Dornick and Associates Business Card

A business card that can be templates for all employees using our newly created logo and information. We are looking for stylish however simplistic in nature, clean looks are better than over the top, however creativity will be appreciated if it has the right appeal. Note: If you feel a type of card (plastic, metalic, carbon, raised lettering, etc) helps your design please specify.
Target Market(s)
Investigation ETC
Industry/Entity Type
Private Investigator
Contact Information for Business Card
Len Dornick
President
5173 Wexbury Road
Hermitage PA 16390-4412
Cell: 724-555-0193; Office: 724-555-0147
Email: lendornick@dornickassociates.example
Font styles to use
Requirements
Must have
- Website DornickAssociates.example
- Name, address, phone number ETC
- Use of current Logo and color pallets if applicable
- TM By logo, small

Nice to have
- Would like to see with and without a photo on the design

Should not have
- Redesign of logo, changing of colors

```html
<!DOCTYPE html>
<html lang="en">
<head>
<meta charset="utf-8">
<title>Dornick and Associates Business Card</title>
<link rel="stylesheet" href="https://fonts.googleapis.com/css2?family=Lato:wght@400;700;900&display=swap">
<style>
  :root {
    --bg: #8c8b8c;
    --card-white: #ffffff;
    --silver-light: #f2f2f3;
    --silver-mid: #d4d4d6;
    --silver-dark: #a9a9ad;
    --emboss: #b9b9bc;
    --brand-red: #d8332a;
    --brand-orange: #ef6a23;
    --ink: #2b2b2b;
    --swoosh-dark: #6f6f72;
  }
  * { box-sizing: border-box; margin: 0; padding: 0; }
  html, body { width: 1200px; height: 900px; overflow: hidden; }
  body {
    background: var(--bg);
    font-family: "Lato", sans-serif;
    position: relative;
  }
  .card {
    position: absolute;
    width: 540px;
    height: 310px;
    border-radius: 14px;
    overflow: hidden;
    box-shadow: 0 6px 14px rgba(0,0,0,.28);
  }
  /* Back side */
  .card-back {
    left: 40px; top: 295px;
    background: linear-gradient(160deg, var(--silver-light) 0%, var(--silver-mid) 55%, var(--silver-dark) 100%);
  }
  .back-brand {
    position: absolute;
    left: 0; right: 0; top: 112px;
    text-align: center;
    font-weight: 900;
    font-size: 34px;
    letter-spacing: 1px;
    color: var(--emboss);
    text-transform: uppercase;
  }
  .back-url {
    position: absolute;
    left: 0; right: 0; top: 236px;
    text-align: center;
    font-size: 13px;
    color: #8e8e91;
  }
  /* Front side */
  .card-front {
    left: 620px; top: 295px;
    background: var(--card-white);
  }
  .swoosh { position: absolute; inset: 0; }
  .portrait {
    position: absolute;
    right: 28px; top: 26px;
    width: 170px; height: 180px;
    border-radius: 40px 40px 10px 10px;
    background: linear-gradient(180deg, #d9b7a2 0%, #c9a48f 32%, #9fb5d8 36%, #8aa4cf 100%);
    opacity: .85;
  }
  .brand {
    position: absolute;
    left: 24px; top: 80px;
    display: flex; align-items: center; gap: 8px;
  }
  .brand-mark {
    width: 14px; height: 14px; border-radius: 50%;
    background: var(--brand-red);
  }
  .brand-name {
    font-weight: 900;
    font-size: 19px;
    color: var(--brand-red);
    text-transform: uppercase;
  }
  .brand-tm {
    font-size: 8px; color: var(--ink);
    align-self: flex-start;
  }
  .person {
    position: absolute;
    left: 24px; top: 116px;
  }
  .person-name { font-size: 24px; font-weight: 700; color: var(--brand-red); line-height: 1.1; }
  .person-title { font-size: 14px; color: var(--ink); }
  .address {
    position: absolute;
    left: 24px; top: 198px;
    font-size: 12px; color: var(--ink); line-height: 1.3;
    font-style: normal;
  }
  .contacts {
    position: absolute;
    left: 24px; top: 234px;
    list-style: none;
    font-size: 12px; color: var(--ink);
  }
  .contacts li { display: flex; align-items: center; gap: 7px; height: 16px; }
  .contacts svg { width: 12px; height: 12px; fill: none; stroke: var(--brand-orange); stroke-width: 2; }
</style>
</head>
<body>

<section class="card card-back" aria-label="Card back">
  <div class="back-brand">Dornick and Associates</div>
  <div class="back-url">www.DornickAssociates.example</div>
</section>

<section class="card card-front" aria-label="Card front">
  <svg class="swoosh" viewBox="0 0 540 310" preserveAspectRatio="none" aria-hidden="true">
    <defs>
      <linearGradient id="lowerGrey" x1="0" y1="0" x2="0" y2="1">
        <stop offset="0" stop-color="#e6e6e7"/>
        <stop offset="1" stop-color="#c2c2c4"/>
      </linearGradient>
    </defs>
    <rect width="540" height="310" fill="#f1f1f2"/>
    <path d="M0 180 C140 140 330 120 540 128 L540 310 L0 310 Z" fill="var(--swoosh-dark)"/>
    <path d="M0 190 C150 152 340 134 540 140 L540 310 L0 310 Z" fill="url(#lowerGrey)"/>
  </svg>

  <div class="portrait" role="img" aria-label="Portrait photo of Len Dornick in a blue polo shirt, arms crossed"></div>

  <div class="brand">
    <span class="brand-mark"></span>
    <span class="brand-name">Dornick and Associates</span>
    <span class="brand-tm">TM</span>
  </div>

  <div class="person">
    <div class="person-name">Len Dornick</div>
    <div class="person-title">President</div>
  </div>

  <address class="address">
    5173 Wexbury Road<br>
    Kestrel Ridge NT 16390-4412
  </address>

  <ul class="contacts">
    <li><svg viewBox="0 0 14 14"><rect x="3.5" y="1" width="7" height="12" rx="1.5"/></svg>555-555-0193</li>
    <li><svg viewBox="0 0 14 14"><path d="M2 2 L5 2 L6 5 L4.5 6.5 Q6 9 7.5 9.5 L9 8 L12 9 L12 12 Q6 12.5 2 2 Z"/></svg>555-555-0147</li>
    <li><svg viewBox="0 0 14 14"><rect x="1" y="3" width="12" height="8"/><path d="M1 3 L7 8 L13 3"/></svg>lendornick@dornickassociates.example</li>
    <li><svg viewBox="0 0 14 14"><circle cx="7" cy="7" r="5.5"/><path d="M1.5 7 H12.5 M7 1.5 Q4 7 7 12.5 Q10 7 7 1.5"/></svg>www.DornickAssociates.example</li>
  </ul>
</section>

</body>
</html>
```